Personal coach needs brochure design for inspirational essay about authenticity

Overview:
I want a beautiful brochure, 11”x17” that folds to 8-1/2”x11” with 4 pages. Think of it as an oversize greeting card.
• Front cover: photograph of a dancer and title with attribution of quote (Lumafold jpeg photo attached)
• Inside spread: Copy (Helena Brisk copy attached) with some appropriate illustration, based on cover photo
• Back cover: contact information, brief descriptive copy, two small photos (jpeg photo attached; see copy for direction)
Copy for front cover title, inside spread and back cover is attached in doc titled "Helena Brisk copy"

Purpose of brochure:
I'm a personal coach and once a year I produce a 4-page illustrated inspirational essay, which invites personal reflection on living a more mindful, meaningful life. Most people I send them to collect them. Someday in the future I'd like to put a collection of these essays into a coffee table book and also create a website for the collection, which is related to the personal coaching that I do.
I have the brochures printed hard copy. I have attached a few examples from previous years. Each has a unique design related to its theme.

Concept:
This year’s essay theme, “There will only ever be one you!” is based on a quote by Helena Brisk, a famous modern dancer. The complete quote, which appears in the copy, is about being true to one’s authentic self. The essay is not about dance, but because the author of the quote was a dancer who personified this theme of being unique to self, I have selected a photo of dance for the cover.

Design Guidance:
Front cover: One possibility is to expand the background color of the Lumafold photo so the photo seems to emerge from the background. But I am open to ideas. I think the photo is artsy enough as it is, but there may be other ways to treat it (e.g. special effects) that would also work. The title should appear somewhere. Make the attribution (--Helena Brisk) in smaller type than the title.

Inside Spread: There may be ways to borrow a design motif from the cover photo to make the inside spread more visually interesting, i.e., not just straight copy. I think it may be helpful to make the font size of the quote larger than the rest of the copy, but it has to be read in sequence. Or maybe it's printed in same size as copy, but then also repeated and displayed by itself in larger type.

Back cover: If you look at some of the other examples I’ve sent, you’ll see how the back cover is typically handled. I want a reduced version of the cover to be placed near the line that says "this is the 16th in a series.." Then, there’s a jpeg photo of Helena Brisk that should be placed next to the copy description of her.

Need extra days to review

```html
<!DOCTYPE html>
<html lang="en">
<head>
<meta charset="utf-8">
<title>There Will Only Ever Be One You — Inside Spread</title>
<link rel="stylesheet" href="https://fonts.googleapis.com/css2?family=Didact+Gothic&family=Quicksand:wght@300&display=swap">
<style>
  :root {
    --ink: #1c1c1c;
    --accent: #5e86b3;
    --band: #6287b0;
    --band-text: #f4f7fb;
    --ring: #a9bfd3;
    --ring-dark: #8ea8c1;
    --paper: #ffffff;
  }
  * { margin: 0; padding: 0; box-sizing: border-box; }
  html, body { width: 929px; height: 1200px; overflow: hidden; background: var(--paper); }
  .page { position: relative; width: 929px; height: 1200px; overflow: hidden; font-family: "Didact Gothic", "Century Gothic", sans-serif; }

  .heading-flourish { position: absolute; left: 70px; top: 70px; width: 20px; height: 74px; }
  .heading {
    position: absolute; left: 102px; top: 68px;
    font-family: "Quicksand", "Century Gothic", sans-serif; font-weight: 300;
    font-size: 34px; line-height: 37px; letter-spacing: -1.2px;
    color: var(--accent); text-transform: uppercase;
  }

  .copy { position: absolute; left: 103px; width: 780px; font-size: 17.4px; line-height: 24.5px; white-space: nowrap; letter-spacing: -0.15px; }
  .intro { top: 150px; color: var(--ink); }
  .intro p + p { margin-top: 24px; }
  .intro .inline-quote { color: var(--accent); }

  .photo-rings { position: absolute; left: 0; top: 300px; width: 929px; height: 340px; }

  .quote { top: 653px; color: var(--accent); }

  .reflection-band { position: absolute; left: 2px; top: 858px; width: 927px; height: 342px; background: var(--band); }
  .band-ornament { position: absolute; left: 101px; top: 895px; width: 156px; height: 18px; }
  .reflection { top: 931px; color: var(--band-text); letter-spacing: -0.3px; }
  .reflection p + p { margin-top: 24px; }
</style>
</head>
<body>
<main class="page">
  <svg class="heading-flourish" viewBox="0 0 20 74" role="img" aria-label="Vertical floral flourish">
    <rect x="6" y="0" width="8" height="74" rx="4" fill="#9db6cf"/>
  </svg>
  <h1 class="heading">In her biography<br>of Brisk,</h1>

  <section class="copy intro">
    <p>her friend and equally talented choreographer Clara Vennett recalled that despite<br>
    sensational reviews for her own innovative work in the Broadway musical Prairie Song!,<br>
    de Vennett had a gnawing feeling that her work was only mediocre.</p>
    <p>De Vennett confessed her anxieties to Brisk who listened quietly and then<br>
    responded, <span class="inline-quote">“There will only ever be one you!”</span> Continuing, she added:</p>
  </section>

  <svg class="photo-rings" viewBox="0 300 929 340">
    <defs>
      <radialGradient id="shade-soft" cx="50%" cy="50%" r="60%">
        <stop offset="0" stop-color="#a6afb8"/><stop offset="1" stop-color="#7f8a95"/>
      </radialGradient>
      <radialGradient id="shade-mid" cx="50%" cy="50%" r="60%">
        <stop offset="0" stop-color="#8794a2"/><stop offset="1" stop-color="#5f6b78"/>
      </radialGradient>
      <radialGradient id="shade-deep" cx="45%" cy="50%" r="60%">
        <stop offset="0" stop-color="#8a7564"/><stop offset="0.5" stop-color="#5a5755"/><stop offset="1" stop-color="#404448"/>
      </radialGradient>
    </defs>
    <g role="img" aria-label="Faded photo of a dancer leaping, seen from above">
      <circle cx="205" cy="474" r="98" fill="url(#shade-soft)" stroke="#c3d2e0" stroke-width="5"/>
    </g>
    <g role="img" aria-label="Photo of the dancer mid-leap in a flowing grey skirt">
      <circle cx="407" cy="474" r="118" fill="url(#shade-mid)" stroke="var(--ring)" stroke-width="6"/>
    </g>
    <g role="img" aria-label="Close-up photo of the dancer's arm and flying blonde hair">
      <circle cx="676" cy="474" r="158" fill="url(#shade-deep)" stroke="var(--ring-dark)" stroke-width="6"/>
    </g>
  </svg>

  <blockquote class="copy quote">
    “There is a vitality, a life-force, an energy, a quickening that is translated through<br>
    you into action.  And because there is only one of you in all of time, this expression<br>
    is unique.  And if you block it, the world will not have it. It is not your business<br>
    to determine how good it is nor how valuable nor how it compares with other<br>
    expressions. It is your business to keep it yours clearly and directly, to keep the<br>
    channel open. You have to keep open and aware directly to the urges that<br>
    motivate you.  Above all else, keep the channel open!”
  </blockquote>

  <div class="reflection-band"></div>
  <svg class="band-ornament" viewBox="0 0 156 18" role="img" aria-label="Horizontal scrollwork ornament">
    <rect x="0" y="5" width="156" height="8" rx="4" fill="#dfe7f0"/>
  </svg>
  <section class="copy reflection">
    <p>Brisk’s wisdom reminds us that we must not hold back or judge our gifts.<br>
    Although there may be moments when we doubt ourselves or when we worry that<br>
    we’re not good enough, our job is to be fearless and to “keep the channel open.”<br>
    Guard the precious miracle of your own uniqueness.</p>
    <p>Find that home-sweet-home feeling  where you feel you are your most authentic self.<br>
    There will only ever be one you!  And importantly, respect the differences of others.<br>
    Our world would be a drab, boring place if we all  only whistled one tune.</p>
  </section>
</main>
</body>
</html>
```